Business Cards and Letterhead for Solo Attorney
Mark Whitfield, Esq., APC
Business Cards and Letterhead for Solo Attorney - Law
Creative Brief
Professional
SEE ADDITIONAL COMMENTS BELOW
742 S. Milbrook Avenue West Covina, CA 91790
mark@whitfieldlegal.example
NAME/TITLE SHOULD APPEAR AS FOLLOWS: Mark Whitfield Attorney at Law/Abogado Workers' Compensation Law It should also have my corporate name somewhere: Mark Whitfield, Esq., APC

```html
<!DOCTYPE html>
<html lang="en">
<head>
<meta charset="utf-8">
<title>Mark Whitfield, Esq., APC — Business Cards</title>
<link rel="stylesheet" href="https://fonts.googleapis.com/css2?family=Oswald:wght@500;700&family=Open+Sans:wght@400;600&display=swap">
<style>
  :root {
    --navy: #1f3a93;
    --white: #ffffff;
    --ink-soft: #dfe6fb;
    --backdrop: #e9e6e1;
  }
  * { margin: 0; padding: 0; box-sizing: border-box; }
  html, body { width: 1200px; height: 794px; overflow: hidden; }
  body {
    background: var(--backdrop);
    display: flex;
    align-items: center;
    justify-content: center;
    gap: 60px;
    font-family: "Open Sans", Arial, sans-serif;
  }
  .card {
    width: 525px;
    height: 300px;
    border-radius: 16px;
    overflow: hidden;
    position: relative;
    box-shadow: 0 10px 28px rgba(0,0,0,0.18);
  }

  /* Front */
  .card-front { background: var(--white); display: flex; flex-direction: column; }
  .front-brand {
    height: 50%;
    display: flex;
    flex-direction: column;
    align-items: center;
    justify-content: center;
    gap: 8px;
  }
  .brand-mark { display: flex; align-items: center; gap: 8px; }
  .brand-dot { width: 14px; height: 14px; border-radius: 50%; background: var(--navy); }
  .brand-name {
    font-family: "Oswald", "Arial Narrow", sans-serif;
    font-weight: 700;
    font-size: 24px;
    letter-spacing: 3px;
    color: var(--navy);
  }
  .firm-name {
    font-family: "Oswald", "Arial Narrow", sans-serif;
    font-weight: 700;
    font-size: 17px;
    letter-spacing: 1.5px;
    color: var(--navy);
  }
  .front-details {
    height: 50%;
    background: var(--navy);
    color: var(--white);
    padding: 16px 26px;
    display: flex;
    justify-content: space-between;
    gap: 16px;
    font-size: 10.5px;
    line-height: 1.5;
  }
  .person-name { font-family: "Oswald", "Arial Narrow", sans-serif; font-weight: 500; font-size: 18px; line-height: 1.2; }
  .person-title { color: var(--ink-soft); }
  .person-address { margin-top: 8px; }
  .contact-list { list-style: none; display: flex; flex-direction: column; gap: 3px; align-self: flex-end; }
  .contact-list li { display: flex; align-items: center; gap: 7px; white-space: nowrap; }
  .contact-list svg { width: 11px; height: 11px; flex: none; }

  /* Back */
  .card-back {
    background: var(--navy);
    color: var(--white);
    display: flex;
    flex-direction: column;
    align-items: center;
    justify-content: center;
  }
  .back-mark { display: flex; align-items: center; gap: 16px; margin-bottom: 40px; }
  .back-mark .brand-dot { width: 30px; height: 30px; background: var(--white); }
  .back-mark .brand-name { font-size: 64px; color: var(--white); letter-spacing: 6px; }
  .back-footer {
    position: absolute;
    right: 26px;
    bottom: 22px;
    text-align: right;
  }
  .back-footer .firm-name { color: var(--white); font-size: 19px; }
  .web { font-size: 11px; color: var(--ink-soft); letter-spacing: 1px; }
</style>
</head>
<body>
  <section class="card card-front" aria-label="Business card front">
    <div class="front-brand">
      <div class="brand-mark">
        <span class="brand-dot"></span>
        <span class="brand-name">WHITFIELD</span>
      </div>
      <p class="firm-name">MARK WHITFIELD ESQ., APC</p>
    </div>
    <div class="front-details">
      <div class="person">
        <p class="person-name">Mark Whitfield</p>
        <p class="person-title">Attorney at Law / Abogado</p>
        <p class="person-title">Workers' Compensation Law</p>
        <p class="person-address">742 S. Milbrook Avenue<br>Ashford Hills, CA 90000</p>
      </div>
      <ul class="contact-list">
        <li><svg viewBox="0 0 12 12"><path fill="#fff" d="M2.5 1 4.5 1 5.3 3.6 4 4.6C4.7 6 6 7.3 7.4 8L8.4 6.7 11 7.5 11 9.5C11 10.3 10.3 11 9.5 11 5 11 1 7 1 2.5 1 1.7 1.7 1 2.5 1Z"/></svg>T (555) 010-0142</li>
        <li><svg viewBox="0 0 12 12"><rect x="1.5" y="3" width="9" height="6" rx="1" fill="none" stroke="#fff" stroke-width="1.2"/><rect x="3.5" y="1" width="5" height="2.5" fill="#fff"/></svg>F (555) 010-0143</li>
        <li><svg viewBox="0 0 12 12"><rect x="1" y="2.5" width="10" height="7" rx="1" fill="none" stroke="#fff" stroke-width="1.2"/><path d="M1.5 3 6 6.5 10.5 3" fill="none" stroke="#fff" stroke-width="1.2"/></svg>mark@whitfieldlegal.example</li>
        <li><svg viewBox="0 0 12 12"><circle cx="6" cy="6" r="4.8" fill="none" stroke="#fff" stroke-width="1.2"/><path d="M1.2 6h9.6M6 1.2c-2.6 3-2.6 6.6 0 9.6M6 1.2c2.6 3 2.6 6.6 0 9.6" fill="none" stroke="#fff" stroke-width="0.9"/></svg>www.whitfieldlegal.example</li>
      </ul>
    </div>
  </section>

  <section class="card card-back" aria-label="Business card back">
    <div class="back-mark">
      <span class="brand-dot"></span>
      <span class="brand-name">WHITFIELD</span>
    </div>
    <div class="back-footer">
      <p class="firm-name">MARK WHITFIELD ESQ., APC</p>
      <p class="web">www.whitfieldlegal.example</p>
    </div>
  </section>
</body>
</html>
```